I need a website built for my organization.
We are the world's largest network of music producers.
The website should be professional, sharp, and high quality., We need a website built for The Harbor Sound Guild. We are one of the World's largest association of music producers.
The site must be professional, sharp, and high quality., I need a website built for my organization.
The site must be professional, sharp, and high quality.
Somewhere in the top half of the site there should be a form for the user to fill out. The details of the form are as follows:
Title (large and bold): Contact Us or Submit Your Music
Fields to include (* = required): First Name*, Last Name*, Age, Zip Code, Email Address*, Daytime Phone, Evening Phone, Comments
Then, there will be a "submit" button to proceed to next step of form. Just below the "submit" button, should be the following verbiage: "After submitting, you will have the opportunity to upload demos of your music (optional) and provide other pertinent information about yourself, band, or group."
Target Market(s)
Music producers and aspiring musicians
Industry/Entity Type
Group
Colors
Designer to choose colors to be used in the design.
Look and feel
Each slider illustrates characteristics of the customer's brand and the style your logo design should communicate.

```html
<!DOCTYPE html>
<html lang="en">
<head>
<meta charset="utf-8">
<title>The Harbor Sound Guild</title>
<link href="https://fonts.googleapis.com/css2?family=Open+Sans:wght@300;400;600;700&display=swap" rel="stylesheet">
<style>
  :root {
    --ink: #3a3a3a;
    --muted: #8a8a8a;
    --logo-grey: #5a5a5a;
    --orange: #f47a20;
    --accent-orange: #f7890c;
    --red: #e8000d;
    --nav-bg: #060606;
    --white: #ffffff;
    --content-bg: #f3f3f3;
    --panel-bg: #ebebeb;
    --field-bg: #d9d9db;
    --field-border: #cfcfd2;
    --placeholder: #6e6e6e;
  }
  * { box-sizing: border-box; margin: 0; padding: 0; }
  html, body { width: 1200px; height: 900px; overflow: hidden; }
  body {
    position: relative;
    font-family: "Open Sans", Arial, sans-serif;
    background: var(--white);
    color: var(--ink);
  }

  /* Header */
  .site-header { position: absolute; top: 0; left: 0; width: 1200px; height: 83px; background: var(--white); }
  .brand {
    position: absolute; left: 33px; top: 26px;
    font-size: 24px; font-weight: 700; color: var(--logo-grey);
    letter-spacing: 0.2px;
  }
  .account-links {
    position: absolute; left: 881px; top: 32px;
    font-size: 12px; font-weight: 700; color: var(--muted); letter-spacing: 0.3px;
  }
  .header-cta {
    position: absolute; left: 1004px; top: 22px; width: 183px; height: 37px;
    background: var(--orange); color: var(--white); border-radius: 3px;
    font-size: 15px; font-weight: 700; text-align: center; line-height: 35px;
  }

  /* Navigation */
  .main-nav { position: absolute; top: 83px; left: 0; width: 1200px; height: 48px; background: var(--nav-bg); }
  .main-nav a {
    position: absolute; top: 0; line-height: 48px; transform: translateX(-50%);
    color: var(--white); font-size: 14px; font-weight: 700; text-decoration: none; letter-spacing: 0.2px;
  }

  /* Hero */
  .hero { position: absolute; top: 131px; left: 0; width: 1200px; height: 445px; background: var(--nav-bg); }
  .hero-photo {
    position: absolute; top: 0; left: 0; width: 1200px; height: 406px;
    background:
      radial-gradient(ellipse at 50% 8%, #2f8fae 0%, rgba(47,143,174,0) 18%),
      linear-gradient(180deg, #6a6e70 0%, #8a6a3e 30%, #5d4526 55%, #2b2118 78%, #120e0c 100%);
  }
  .hero-copy { position: absolute; top: 214px; left: 0; width: 1200px; text-align: center; }
  .hero-title { font-size: 46px; font-weight: 300; color: var(--white); line-height: 56px; margin-left: -10px; }
  .hero-title strong { display: block; font-weight: 700; color: var(--accent-orange); }
  .hero-join {
    display: inline-block; margin-top: 0; font-size: 24px; font-weight: 700;
    color: var(--red); text-decoration: underline; text-decoration-thickness: 2px; line-height: 36px;
  }

  /* Content */
  .welcome { position: absolute; top: 576px; left: 0; width: 782px; height: 324px; background: var(--content-bg); }
  .welcome h1 { position: absolute; left: 33px; top: 21px; font-size: 28px; font-weight: 400; color: #4a4a4a; }
  .welcome p { position: absolute; left: 36px; width: 682px; font-size: 14px; line-height: 24px; color: var(--ink); }
  .welcome .intro { top: 79px; }
  .welcome .more { top: 272px; left: 40px; width: 678px; }

  /* Form panel */
  .submit-panel { position: absolute; top: 576px; left: 782px; width: 406px; height: 324px; background: var(--panel-bg); }
  .submit-panel h2 { position: absolute; left: 17px; top: 24px; font-size: 20px; font-weight: 700; color: var(--red); }
  .field {
    position: absolute; left: 19px; width: 370px; height: 41px;
    background: var(--field-bg); border: 1px solid var(--field-border);
    font-family: inherit; font-size: 14px; color: var(--placeholder); padding-left: 20px;
  }
  .field::placeholder { color: var(--placeholder); }
  .edge-strip { position: absolute; top: 576px; left: 1188px; width: 12px; height: 324px; background: #f6f6f6; }
</style>
</head>
<body>
  <header class="site-header">
    <div class="brand">The Harbor Sound Guild</div>
    <div class="account-links">LOGIN | REGISTER</div>
    <a class="header-cta">Submit your Music</a>
  </header>

  <nav class="main-nav">
    <a style="left:424px">HOME</a>
    <a style="left:535px">ABOUT</a>
    <a style="left:639px">NEWS</a>
    <a style="left:773px">MEMBERSHIP</a>
    <a style="left:897px">EVENTS</a>
    <a style="left:1019px">RESOURCES</a>
    <a style="left:1156px">CONTACT</a>
  </nav>

  <section class="hero">
    <div class="hero-photo" role="img" aria-label="Producer seen from behind at a mixing console, looking into a large recording hall with an orchestra"></div>
    <div class="hero-copy">
      <h2 class="hero-title">The World's Largest Network of<strong>Music Producers</strong></h2>
      <a class="hero-join">Join Now</a>
    </div>
  </section>

  <main class="welcome">
    <h1>Welcome</h1>
    <p class="intro">Lorem Ipsum is simply dummy text of the printing and typesetting industry. Lorem Ipsum has been the industry's standard dummy text ever since the 1500s, when an unknown printer took a galley of type and scrambled it to make a type specimen book. It has survived not only five centuries, but also the leap into electronic typesetting, remaining essentially unchanged. It was popularised in the 1960s with the release of Presstype sheets containing Lorem Ipsum passages, and more recently with desktop publishing software like Folio Layout including versions of Lorem Ipsum.</p>
    <p class="more">It was popularised in the 1960s with the release of Presstype sheets containing Lorem Ipsum passages, and more recently with desktop publishing software like Folio Layout including versions of Lorem Ipsum.</p>
  </main>

  <aside class="submit-panel">
    <h2>Submit your Music !</h2>
    <input class="field" style="top:79px" placeholder="First Name">
    <input class="field" style="top:146px" placeholder="Last Name">
    <input class="field" style="top:214px" placeholder="Age">
    <input class="field" style="top:279px" placeholder="Zip Code">
  </aside>
  <div class="edge-strip"></div>
</body>
</html>
```